azure haven of northeast florida business card

I need a new attractive business card. I am planning on printing on very thick rounded corner stock and having painted edges. We are a swimming pool remodel, repair, and service company in north florida. Our current logo is red, white, and blue. It doesn't necessarily have to stay that way, I am open to other ideas. It will need to contain my name, work and cell numbers, email, website, and my contractor license number.

Target Market(s)

High end residential and commercial clients

Industry/Entity Type

Business

Contact Information for Business Card

Company name, employee name and title, work and cell phone numbers, email and website, and Contractor number.

our work scope should be on card somewhere: remodel ~ repair ~ service

logo or slight variation of logo also. (not necessarily set on keeping exact logo)

Colors

Designer to choose colors to be used in the design.

Requirements
Nice to have
• We deal with water so I think some sort of water element or just a color similar to pool water would be nice to integrate into design.

```html
<!DOCTYPE html>
<html lang="en">
<head>
<meta charset="utf-8">
<title>Azure Haven of Northeast Florida – Business Card</title>
<link rel="stylesheet" href="https://fonts.googleapis.com/css2?family=Roboto:wght@400;500;700&display=swap">
<style>
  :root {
    --page-bg: #e6e8ea;
    --pool-deep: #0f5aa6;
    --pool-mid: #2474c2;
    --pool-light: #4a93d6;
    --brand-blue: #1b6bb0;
    --brand-red: #e43a45;
    --ink-grey: #555b60;
    --splash-tint: #e6eff8;
    --rule-blue: #5d97c9;
    --white: #ffffff;
  }
  * { box-sizing: border-box; margin: 0; padding: 0; }
  html, body { width: 1200px; height: 1000px; overflow: hidden; }
  body { background: var(--page-bg); font-family: "Roboto", Arial, sans-serif; position: relative; }

  .card { position: absolute; left: 270px; width: 661px; height: 379px; overflow: hidden;
          box-shadow: 0 4px 12px rgba(0,0,0,.18); }
  .card-front { top: 108px; }
  .card-back { top: 520px; background: var(--white); }

  .water-surface { position: absolute; inset: 0;
    background: radial-gradient(ellipse at 60% 40%, var(--pool-light) 0%, var(--pool-mid) 40%, var(--pool-deep) 100%); }

  .brand { position: absolute; display: flex; align-items: center; }
  .brand-dot { border-radius: 50%; background: var(--brand-red); flex: none; }
  .brand-name { font-weight: 500; text-transform: uppercase; line-height: 1; }
  .brand-name .main { display: block; }
  .brand-name .sub { display: block; }

  .card-front .brand { left: 93px; top: 149px; }
  .card-front .brand-dot { width: 80px; height: 80px; margin-right: 15px; }
  .card-front .brand-name { color: var(--white); }
  .card-front .brand-name .main { font-size: 38px; letter-spacing: 4px; }
  .card-front .brand-name .sub { font-size: 16px; letter-spacing: 5.2px; margin-top: 8px; }

  .services { position: absolute; left: 0; right: 0; top: 322px; text-align: center;
              color: var(--white); font-size: 15px; }
  .services .sep { display: inline-block; width: 7px; height: 7px; border-radius: 50%;
                   background: var(--brand-red); margin: 0 8px; vertical-align: middle; }

  .card-back .brand { left: 36px; top: 45px; }
  .card-back .brand-dot { width: 60px; height: 60px; margin-right: 10px; }
  .card-back .brand-name { color: var(--brand-blue); }
  .card-back .brand-name .main { font-size: 29px; letter-spacing: 3px; }
  .card-back .brand-name .sub { font-size: 12.5px; letter-spacing: 4px; margin-top: 5px; }

  .splash-art { position: absolute; left: 385px; top: 10px; width: 276px; height: 305px;
    background: radial-gradient(ellipse at 50% 55%, var(--splash-tint) 0%, rgba(230,239,248,.5) 55%, rgba(255,255,255,0) 75%); }

  .person { position: absolute; right: 38px; top: 162px; text-align: right; }
  .person-name { color: var(--brand-red); font-weight: 700; font-size: 19px; }
  .person-title { color: var(--ink-grey); font-size: 14.5px; margin-top: 4px; }
  .divider { position: absolute; left: 40px; width: 520px; top: 196px; height: 1px; background: var(--rule-blue); }

  .contacts { position: absolute; left: 36px; top: 212px; list-style: none; color: var(--ink-grey); font-size: 15px; }
  .contacts li { height: 21px; display: flex; align-items: center; }
  .contacts svg { width: 11px; height: 11px; margin-right: 5px; fill: var(--brand-blue); }

  .waves { position: absolute; left: 0; bottom: 0; width: 661px; height: 380px; }
  .license { position: absolute; left: 393px; top: 339px; color: var(--white); font-size: 15px; }
</style>
</head>
<body>

<section class="card card-front">
  <div class="water-surface" role="img" aria-label="Rippling blue swimming pool water"></div>
  <div class="brand">
    <span class="brand-dot"></span>
    <span class="brand-name"><span class="main">Azure Haven</span><span class="sub">of Northeast Florida</span></span>
  </div>
  <p class="services">Remodel<span class="sep"></span>Repair<span class="sep"></span>Service</p>
</section>

<section class="card card-back">
  <div class="splash-art" role="img" aria-label="Faint water splash decoration"></div>
  <div class="brand">
    <span class="brand-dot"></span>
    <span class="brand-name"><span class="main">Azure Haven</span><span class="sub">of Northeast Florida</span></span>
  </div>

  <div class="person">
    <p class="person-name">Daniel Reyes</p>
    <p class="person-title">President</p>
  </div>
  <div class="divider"></div>

  <ul class="contacts">
    <li><svg viewBox="0 0 12 12"><path d="M2.5 0.8 L4.3 2.9 L3.3 4.2 Q4.4 6.6 7.8 8.7 L9.1 7.7 L11.2 9.5 L10 11.2 Q4.5 10.6 0.8 2 Z"/></svg>407.555.0142</li>
    <li><svg viewBox="0 0 12 12"><path d="M3 0 H9 V12 H3 Z M4 1.5 V9.5 H8 V1.5 Z" fill-rule="evenodd"/></svg>407.555.0187</li>
    <li><svg viewBox="0 0 12 12"><path d="M0 2 H12 V10 H0 Z M0.8 2.6 L6 6.6 L11.2 2.6 Z" fill-rule="evenodd"/></svg>info@azurehaven.com</li>
    <li><svg viewBox="0 0 12 12"><circle cx="6" cy="6" r="5.5"/><path d="M0.8 6 H11.2 M6 0.6 V11.4 M2 3.3 H10 M2 8.7 H10" stroke="#fff" stroke-width="0.8" fill="none"/></svg>www.azurehaven.com</li>
  </ul>

  <svg class="waves" viewBox="0 0 661 380" aria-hidden="true">
    <path d="M0 346 Q 240 378 400 318 Q 520 290 661 306 L661 380 L0 380 Z" fill="var(--pool-mid)"/>
    <path d="M0 302 Q 70 372 295 330 Q 110 385 0 335 Z" fill="var(--brand-red)"/>
  </svg>
  <p class="license">Contractor No: #581907</p>
</section>

</body>
</html>
```